I need a CD cover (simple single CD -- NOT jewel case) for my new CD. This is a very small independent project -- probably 100 - 200 copies to be made in total. The name of the CD is "Folded Lanterns". My name (artist) is vel marsh (I prefer lower case for my name). I just want an interesting design on the front cover that has both the CD name and my name (no photo) -- just something that looks cool -- I'm open to any and all ideas. The back should contain the enclosed photo -- I am open to the photo being any size -- even very small if that looks best. The front cover design will also need to be ON the CD itself (adapted as needed). I am not concerned with the design of the front having any relationship to the music -- I just want something that is attractive and looks cool.
Look and feel
Each slider illustrates characteristics of the customer's brand and the style your logo design should communicate.

```html
<!DOCTYPE html>
<html lang="en">
<head>
<meta charset="utf-8">
<title>Folded Lanterns — vel marsh</title>
<link rel="stylesheet" href="https://fonts.googleapis.com/css2?family=Oswald:wght@300&display=swap">
<style>
  :root {
    --sky: #dfe2bf;
    --sky-glow: #eef0cf;
    --brick-dark: #2b2521;
    --brick: #5a3f33;
    --street: #a8495a;
    --street-light: #c98a8e;
    --reflect-dark: #1d1a1c;
    --reflect-warm: #7a3440;
    --reflect-sky: #e3b8a4;
    --type: #ffffff;
  }
  html, body {
    margin: 0;
    padding: 0;
    width: 1200px;
    height: 1200px;
    overflow: hidden;
    background: #000;
  }
  .cover {
    position: relative;
    width: 1200px;
    height: 1200px;
    overflow: hidden;
    font-family: "Oswald", "Arial Narrow", sans-serif;
    font-weight: 300;
    color: var(--type);
  }
  .cover__photo {
    position: absolute;
    inset: 0;
    background:
      /* street surface band */
      linear-gradient(180deg,
        transparent 0 600px,
        var(--street) 610px,
        var(--street-light) 640px,
        var(--street) 668px,
        transparent 680px),
      /* pale sky above, pale sky reflected below */
      linear-gradient(90deg,
        transparent 0 520px,
        var(--sky) 540px,
        var(--sky-glow) 590px,
        var(--sky) 640px,
        transparent 660px) 0 0 / 100% 600px no-repeat,
      linear-gradient(90deg,
        transparent 0 520px,
        var(--reflect-sky) 545px,
        #f0cdb6 590px,
        var(--reflect-sky) 635px,
        transparent 660px) 0 680px / 100% 520px no-repeat,
      /* buildings above the horizon */
      linear-gradient(90deg,
        var(--brick-dark) 0,
        var(--brick) 220px,
        #3a3430 460px,
        #4b433c 700px,
        #8a6b5a 960px,
        #6b5345 1200px) 0 0 / 100% 600px no-repeat,
      /* reflected buildings */
      linear-gradient(90deg,
        var(--reflect-dark) 0,
        #3b2228 240px,
        var(--reflect-warm) 460px,
        #5c2c35 700px,
        #8b4a4d 960px,
        #5e2e33 1200px) 0 680px / 100% 520px no-repeat;
  }
  .cover__photo::after {
    content: "";
    position: absolute;
    inset: 0;
    background: linear-gradient(180deg, rgba(0,0,0,0.15) 0, transparent 30%, transparent 70%, rgba(0,0,0,0.35) 100%);
  }
  .artist {
    position: absolute;
    left: 36px;
    top: 566px;
    font-size: 84px;
    line-height: 1;
    letter-spacing: -1px;
    text-transform: lowercase;
  }
  .artist__name {
    display: block;
  }
  .artist__reflection {
    display: block;
    transform: scaleY(-1);
    margin-top: -30px;
    opacity: 0.35;
    -webkit-mask-image: linear-gradient(0deg, #000 0, transparent 55%);
    mask-image: linear-gradient(0deg, #000 0, transparent 55%);
  }
  .title {
    position: absolute;
    left: 36px;
    top: 1080px;
    margin: 0;
    font-size: 84px;
    font-weight: 300;
    line-height: 1;
    letter-spacing: -1px;
    text-transform: uppercase;
    white-space: nowrap;
  }
</style>
</head>
<body>
  <main class="cover">
    <div class="cover__photo" role="img" aria-label="Photograph of a narrow city alley with brick buildings, fire escapes and dumpsters, mirrored in a large rain puddle on pinkish pavement"></div>
    <div class="artist">
      <span class="artist__name">vel marsh</span>
      <span class="artist__reflection" aria-hidden="true">vel marsh</span>
    </div>
    <h1 class="title">Folded Lanterns</h1>
  </main>
</body>
</html>
```